Need a design for a pull up banner to promote a book

need a design for pull up banner (size 850mm x 2000mm) to promote a new book and the author. It has to be attractive design and grab attention.

I have attached the images of the book and some photos of the author.

my web address: https://corvimbeltra.com

Target Market(s)

Business leaders

```html
<!DOCTYPE html>
<html lang="en">
<head>
<meta charset="utf-8">
<title>Why Stagnation Stings – Pull Up Banner</title>
<link href="https://fonts.googleapis.com/css2?family=Bebas+Neue&family=Questrial&display=swap" rel="stylesheet">
<style>
  :root {
    --backdrop: #2b2b2b;
    --paper: #ffffff;
    --ink: #111111;
    --crimson: #b3132f;
    --crimson-deep: #7d0a1f;
    --night: #1b1b1b;
    --photo-light: #4a4a4a;
    --photo-dark: #161616;
  }
  * { margin: 0; padding: 0; box-sizing: border-box; }
  html, body {
    width: 1200px;
    height: 1177px;
    overflow: hidden;
    background: var(--backdrop);
  }
  .banner {
    position: absolute;
    left: 414px;
    top: 121px;
    width: 398px;
    height: 938px;
    overflow: hidden;
    background: var(--paper);
  }
  .banner-shapes {
    position: absolute;
    inset: 0;
    width: 100%;
    height: 100%;
  }
  .headline {
    position: absolute;
    left: 56px;
    top: 16px;
    width: 292px;
    font-family: "Bebas Neue", "Oswald", sans-serif;
    font-weight: 400;
    line-height: 0.88;
    color: var(--ink);
  }
  .headline span { display: block; }
  .headline-why { font-size: 64px; }
  .headline-key { font-size: 72px; color: var(--crimson); letter-spacing: 0.5px; }
  .headline-verb { font-size: 64px; text-align: right; }
  .book-formats {
    position: absolute;
    left: 76px;
    top: 198px;
    width: 264px;
    height: 228px;
    border-radius: 4px;
    background: linear-gradient(160deg, #f2f2f2 0%, #8c8c8c 45%, #2a2a36 75%, var(--crimson) 100%);
  }
  .author-photo {
    position: absolute;
    left: 0;
    top: 461px;
    width: 196px;
    height: 440px;
    background: linear-gradient(135deg, var(--photo-light), var(--photo-dark));
  }
  .tagline {
    position: absolute;
    left: 200px;
    top: 540px;
    width: 184px;
    font-family: "Questrial", "Helvetica Neue", sans-serif;
    font-size: 18px;
    line-height: 22px;
    text-align: center;
    color: var(--paper);
  }
  .tagline em { font-style: normal; color: var(--crimson); }
  .author-signoff {
    position: absolute;
    right: 18px;
    top: 832px;
    text-align: right;
    font-family: "Questrial", "Helvetica Neue", sans-serif;
    color: var(--paper);
  }
  .author-name { font-size: 28px; line-height: 1; }
  .author-roles {
    margin-top: 6px;
    font-size: 7px;
    letter-spacing: 1px;
    line-height: 1.35;
    text-transform: uppercase;
  }
  .author-web {
    margin-top: 4px;
    font-size: 9px;
    letter-spacing: 0.5px;
  }
</style>
</head>
<body>
  <main class="banner">
    <svg class="banner-shapes" viewBox="0 0 398 938" preserveAspectRatio="none" aria-hidden="true">
      <defs>
        <linearGradient id="mistFade" x1="0" y1="0" x2="0" y2="1">
          <stop offset="0" stop-color="#e4e4e4"/>
          <stop offset="1" stop-color="#c9c9c9"/>
        </linearGradient>
      </defs>
      <path d="M0 165 Q190 120 398 230 L398 420 L0 420 Z" fill="url(#mistFade)"/>
      <rect x="0" y="400" width="398" height="538" fill="var(--night)"/>
      <path d="M0 352 Q200 338 398 350 L398 470 Q220 520 0 430 Z" fill="var(--crimson-deep)"/>
      <path d="M0 347 Q200 333 398 345 L398 450 Q220 500 0 418 Z" fill="var(--crimson)"/>
    </svg>

    <div class="author-photo" role="img" aria-label="Portrait photo of the author in a dark suit, smiling with open hands"></div>

    <svg class="banner-shapes" viewBox="0 0 398 938" preserveAspectRatio="none" aria-hidden="true">
      <path d="M0 858 Q170 800 398 765 L398 938 L0 938 Z" fill="var(--crimson-deep)"/>
      <path d="M0 875 Q170 815 398 780 L398 938 L0 938 Z" fill="var(--crimson)"/>
    </svg>

    <h1 class="headline">
      <span class="headline-why">Why</span>
      <span class="headline-key">Stagnation</span>
      <span class="headline-verb">Stings</span>
    </h1>

    <div class="book-formats" role="img" aria-label="The book shown as tablet, phone and printed paperback editions"></div>

    <p class="tagline">Everything You’ve<br>Worked So Hard<br>to Create Can<br>Disappear Through<br><em>Stagnation</em></p>

    <div class="author-signoff">
      <p class="author-name">Corvim Beltra</p>
      <p class="author-roles">Entrepreneur<br>Keynote Speaker<br>Author</p>
      <p class="author-web">https://corvimbeltra.com</p>
    </div>
  </main>
</body>
</html>
```